We need a business card design for an assisted living facility in Los Angeles. We have a logo selected but we would like a business card design that will leave a lasting impression on families looking to place their elderly loved ones in our care as well as on other facility providers who may refer their elderly residents to our facility.

```html
<!DOCTYPE html>
<html lang="en">
<head>
<meta charset="UTF-8">
<title>Harborview Grace Senior Living – Business Card</title>
<link href="https://fonts.googleapis.com/css2?family=Cinzel:wght@500&family=Poppins:wght@400&display=swap" rel="stylesheet">
<style>
  :root {
    --backdrop: #c4c4c4;
    --card-white: #ffffff;
    --brand-blue: #0079cc;
    --deep-blue: #0a4f86;
    --text-grey: #444444;
    --rule-grey: #9a9a9a;
  }
  * { margin: 0; padding: 0; box-sizing: border-box; }
  html, body {
    width: 1093px;
    height: 1200px;
    overflow: hidden;
    background: var(--backdrop);
  }
  .canvas {
    position: relative;
    width: 1093px;
    height: 1200px;
  }
  .card {
    position: absolute;
    left: 265px;
    width: 578px;
    height: 356px;
    border-radius: 30px;
    overflow: hidden;
  }
  .card--front { top: 226px; background: var(--card-white); }
  .card--back  { top: 621px; background: var(--brand-blue); }

  .brand-name {
    position: absolute;
    font-family: "Cinzel", serif;
    font-weight: 500;
    letter-spacing: 0.04em;
    white-space: nowrap;
    text-align: center;
    line-height: 1.15;
  }
  .card--front .brand-name {
    left: 30px;
    width: 246px;
    top: 148px;
    font-size: 20px;
    color: var(--brand-blue);
  }
  .card--back .brand-name {
    left: 0;
    width: 100%;
    top: 142px;
    font-size: 31px;
    color: var(--deep-blue);
  }

  .divider {
    position: absolute;
    left: 288px;
    top: 74px;
    width: 1px;
    height: 210px;
    background: var(--rule-grey);
  }

  .details {
    position: absolute;
    left: 311px;
    top: 88px;
    font-family: "Poppins", sans-serif;
    color: var(--text-grey);
  }
  .person-name {
    font-family: "Cinzel", serif;
    font-weight: 500;
    font-size: 23px;
    line-height: 26px;
    color: var(--brand-blue);
  }
  .person-title {
    font-size: 17px;
    line-height: 20px;
  }
  .contact-list {
    list-style: none;
    margin-top: 13px;
  }
  .contact-item {
    display: flex;
    align-items: center;
    font-size: 17px;
    line-height: 21px;
  }
  .contact-icon {
    width: 15px;
    height: 15px;
    margin-right: 7px;
    flex: none;
    fill: var(--brand-blue);
  }
  .web-highlight { color: var(--brand-blue); }
  .address {
    margin-top: 13px;
    font-size: 17px;
    line-height: 21px;
    font-style: normal;
  }
</style>
</head>
<body>
<main class="canvas">

  <section class="card card--front" aria-label="Business card front">
    <p class="brand-name">HARBORVIEW GRACE</p>
    <div class="divider"></div>
    <div class="details">
      <h1 class="person-name">DANIEL WHITMORE</h1>
      <p class="person-title">Managing Director</p>
      <ul class="contact-list">
        <li class="contact-item">
          <svg class="contact-icon" viewBox="0 0 24 24" aria-hidden="true"><path d="M6.6 10.8a15 15 0 0 0 6.6 6.6l2.2-2.2a1 1 0 0 1 1-.25 11.4 11.4 0 0 0 3.6.57 1 1 0 0 1 1 1V20a1 1 0 0 1-1 1A17 17 0 0 1 3 4a1 1 0 0 1 1-1h3.5a1 1 0 0 1 1 1c0 1.25.2 2.45.57 3.57a1 1 0 0 1-.25 1z"/></svg>
          310-555 0184
        </li>
        <li class="contact-item">
          <svg class="contact-icon" viewBox="0 0 24 24" aria-hidden="true"><path d="M2 5h20v14H2z M2 5l10 8 10-8" fill="var(--brand-blue)" stroke="#fff" stroke-width="1.5"/></svg>
          care@hvgrace.com
        </li>
        <li class="contact-item">
          <svg class="contact-icon" viewBox="0 0 24 24" aria-hidden="true"><g fill="none" stroke="var(--brand-blue)" stroke-width="2"><circle cx="12" cy="12" r="10"/><ellipse cx="12" cy="12" rx="4.5" ry="10"/><path d="M2 12h20M4 7h16M4 17h16"/></g></svg>
          <span>www.<span class="web-highlight">harborviewgrace</span>.com</span>
        </li>
      </ul>
      <address class="address">1280 Maple Crest Avenue<br>Los Angeles, CA 90024</address>
    </div>
  </section>

  <section class="card card--back" aria-label="Business card back">
    <p class="brand-name">HARBORVIEW GRACE</p>
  </section>

</main>
</body>
</html>
```